Flyer for Fertility Specialty Pharmacy

We need to design a flyer , which contains the information about our Fertility Pharmacy , Services, and Medication pricing. We will be distributing these to Fertility clinics and Patients. We will provide the logo.
http://corvenhale.com/

Fertility Clinics , IVF patients, Other pharmacies

Fertility

• baby pictures , or related to Fertility, IVF etc
• This flyer is to attract couples who are trying for pregnancy.

```html
<!DOCTYPE html>
<html lang="en">
<head>
<meta charset="utf-8">
<title>Corvenhale Twin Pharmacy – Fertility Flyer</title>
<link href="https://fonts.googleapis.com/css2?family=Exo+2:wght@500;600;700;800&family=Montserrat:wght@400;500;600;700&display=swap" rel="stylesheet">
<style>
:root{
  --teal:#16a58a;
  --teal-dark:#0f8c74;
  --teal-deep:#0c7a65;
  --teal-soft:#d9f1ec;
  --yellow:#f5d42a;
  --ink:#1d1d1d;
  --grey:#5a5a5a;
  --row:#e9e9e9;
  --page:#eef0ef;
  --white:#ffffff;
}
*{box-sizing:border-box;margin:0;padding:0}
html,body{width:1200px;height:2400px;overflow:hidden;background:var(--page)}
body{font-family:"Montserrat",sans-serif;color:var(--ink);position:relative}
.spread{position:absolute;left:30px;width:1140px;height:880px;background:var(--white);box-shadow:0 18px 40px rgba(0,0,0,.18);overflow:hidden}
.spread.outside{top:260px}
.spread.inside{top:1260px}
.col{position:absolute;top:0;width:380px;height:880px}
.col.c1{left:0}.col.c2{left:380px}.col.c3{left:760px}
.col.teal{background:var(--teal);color:var(--white)}
.col.tint{background:linear-gradient(180deg,#eef9f7,#ffffff 60%,#eaf6f3)}
.abs{position:absolute}
.photo{position:absolute}
.heading{font-family:"Exo 2",sans-serif;font-weight:700;color:var(--teal);letter-spacing:.5px}
.services-title{left:30px;top:40px;font-size:30px}
.service-list{left:30px;top:92px;width:320px;list-style:none;font-size:14px;line-height:1.25}
.service-list li{position:relative;padding-left:22px;margin-bottom:9px}
.service-list svg{position:absolute;left:0;top:3px}
.pill{position:absolute;background:var(--teal);color:var(--white);border-radius:12px;text-align:center;font-family:"Montserrat",sans-serif;font-weight:500;font-size:17px;line-height:1.15;padding:10px 8px;letter-spacing:.3px}
.brand{position:absolute;display:flex;align-items:center;gap:10px}
.brand .mark{width:22px;height:22px}
.brand .name{font-family:"Exo 2",sans-serif;font-weight:700;line-height:1}
.brand .name small{display:block;font-size:.5em;font-weight:600;margin-top:3px}
.contact{font-family:"Montserrat",sans-serif;font-weight:500;line-height:1.4}
.contact b{font-weight:700}
.url{position:absolute;background:#000;color:var(--white);font-weight:600;font-size:17px;border-radius:6px;padding:3px 12px;letter-spacing:.5px}
.address{position:absolute;font-size:14px;font-weight:500;line-height:1.25;padding-left:20px}
.address svg{position:absolute;left:0;top:1px}
.program{position:absolute;font-family:"Exo 2",sans-serif;font-weight:800;font-size:27px;line-height:1.15}
.title{position:absolute;font-family:"Exo 2",sans-serif;font-weight:700;line-height:1}
.badge-ship{position:absolute;border-radius:50%;background:var(--yellow);border:5px solid #fff2a8;box-shadow:0 4px 10px rgba(0,0,0,.2)}
.meds-title{left:0;width:380px;top:128px;text-align:center;font-size:28px}
.bracket{position:absolute;border:2px solid #9a9a9a}
.med-table{position:absolute;left:0;top:195px;width:380px;border-collapse:collapse;font-size:13.5px}
.med-table td{height:29.5px;padding:0 20px 0 42px;color:#333}
.med-table td.price{text-align:right;padding:0 22px 0 0;width:80px}
.med-table tr:nth-child(odd){background:var(--row)}
.ivf-title{position:absolute;left:0;width:380px;top:20px;text-align:center;font-family:"Exo 2",sans-serif;font-weight:700;font-size:30px;color:var(--white);letter-spacing:1px}
.ivf-box{position:absolute;left:30px;top:40px;width:320px;height:335px;border:2px solid rgba(255,255,255,.8);border-radius:6px}
.ivf-table{position:absolute;left:32px;top:108px;width:316px;border-collapse:collapse;font-size:14px;font-weight:600;color:var(--white)}
.ivf-table td{height:29.5px;padding:0 14px}
.ivf-table tr:nth-child(odd){background:var(--teal-deep)}
.ivf-table tr:nth-child(even){background:var(--teal-dark)}
.ivf-head{position:absolute;left:46px;top:60px;width:288px;display:flex;justify-content:space-between;font-size:15px;font-weight:600;padding-bottom:12px;border-bottom:1px solid rgba(255,255,255,.7)}
.owners{position:absolute;left:30px;top:400px;width:320px;height:208px;background:var(--white);padding:10px}
.owners p{font-size:11px;color:#333;margin-top:6px;font-family:"Montserrat",sans-serif}
.years{position:absolute;left:28px;top:630px;display:flex;align-items:center;gap:6px}
.years .over{writing-mode:vertical-rl;transform:rotate(180deg);font-family:"Exo 2",sans-serif;font-weight:700;font-size:16px}
.years .big{font-family:"Exo 2",sans-serif;font-weight:700;font-size:50px;line-height:1}
.serving{position:absolute;left:28px;top:695px;width:324px;font-family:"Exo 2",sans-serif;font-weight:700;font-size:21px;border-top:2px solid rgba(255,255,255,.8);border-bottom:2px solid rgba(255,255,255,.8);padding:4px 0;letter-spacing:.3px}
.about{position:absolute;left:28px;top:745px;width:324px;font-size:11.5px;line-height:1.3}
.cert{position:absolute;left:40px;top:45px;width:170px;text-align:center}
.cert .seal{width:120px;height:120px;margin:0 auto;border-radius:50%;background:var(--white);border:8px solid var(--yellow);box-shadow:0 0 0 3px #e8c318}
.cert .acc{font-weight:700;font-size:14px;margin-top:8px;color:#333;letter-spacing:.5px}
.cert .exp{font-family:Georgia,serif;font-size:14px;color:#444;line-height:1.2}
</style>
</head>
<body>

<!-- OUTSIDE SPREAD -->
<section class="spread outside">

  <div class="col c1">
    <h2 class="abs heading services-title">SERVICES</h2>
    <ul class="abs service-list">
      <li><svg width="12" height="10" viewBox="0 0 12 10"><path d="M1 5l3.5 3.5L11 1" fill="none" stroke="#16a58a" stroke-width="2.4"/></svg>Fertility specialist Pharmacist on call 24/7</li>
      <li><svg width="12" height="10" viewBox="0 0 12 10"><path d="M1 5l3.5 3.5L11 1" fill="none" stroke="#16a58a" stroke-width="2.4"/></svg>Personal service to all patients</li>
      <li><svg width="12" height="10" viewBox="0 0 12 10"><path d="M1 5l3.5 3.5L11 1" fill="none" stroke="#16a58a" stroke-width="2.4"/></svg>Individual counseling provided for all the patients</li>
      <li><svg width="12" height="10" viewBox="0 0 12 10"><path d="M1 5l3.5 3.5L11 1" fill="none" stroke="#16a58a" stroke-width="2.4"/></svg>Once the patient leaves your office the rest is on us</li>
      <li><svg width="12" height="10" viewBox="0 0 12 10"><path d="M1 5l3.5 3.5L11 1" fill="none" stroke="#16a58a" stroke-width="2.4"/></svg>Initiate and follow up on the prior authorizations.</li>
      <li><svg width="12" height="10" viewBox="0 0 12 10"><path d="M1 5l3.5 3.5L11 1" fill="none" stroke="#16a58a" stroke-width="2.4"/></svg>We have all fertility medications in stock</li>
      <li><svg width="12" height="10" viewBox="0 0 12 10"><path d="M1 5l3.5 3.5L11 1" fill="none" stroke="#16a58a" stroke-width="2.4"/></svg>Free next day delivery via courier to Home or work</li>
    </ul>
    <svg class="abs" style="left:-80px;top:420px" width="380" height="380" viewBox="0 0 380 380">
      <circle cx="190" cy="190" r="180" fill="none" stroke="#16a58a" stroke-width="3"/>
      <circle cx="180" cy="195" r="165" fill="#16a58a"/>
    </svg>
    <div class="photo" role="img" aria-label="Smiling baby sitting in a mint green bodysuit" style="left:20px;top:390px;width:270px;height:470px;border-radius:130px 130px 40px 40px;background:linear-gradient(180deg,#f3d7c3,#bfe7da 55%,#e8d2c0)"></div>
  </div>

  <div class="col c2">
    <div class="pill" style="left:25px;top:18px;width:245px">CONFIDENTIAL PRICING FOR<br>SUMMIT FERTILITY COLORADO</div>
    <div class="photo" role="img" aria-label="Happy family of mother, father and son in a bright kitchen" style="left:0;top:70px;width:300px;height:330px;background:linear-gradient(180deg,#ecebe8,#f4f2ef 60%,#ffffff)"></div>
    <div class="brand" style="left:30px;top:418px;color:var(--teal)">
      <span class="mark" style="border:2px solid var(--teal);border-radius:50%"></span>
      <span class="name" style="font-size:22px">Corvenhale<small>Twin Pharmacy</small></span>
    </div>
    <div class="abs contact" style="left:30px;top:476px;font-size:16px">
      <div><b style="color:var(--teal)">Phone:</b> 609-555-0172</div>
      <div><b style="color:var(--teal)">Toll Free:</b> 800-555-0199</div>
      <div><b style="color:var(--teal)">Fax:</b> 609-555-0148</div>
    </div>
    <div class="url" style="left:30px;top:562px">www.corvenhale.com</div>
    <div class="address" style="left:30px;top:603px">
      <svg width="11" height="14" viewBox="0 0 11 14"><path d="M5.5 0C2.5 0 0 2.4 0 5.4 0 9.3 5.5 14 5.5 14S11 9.3 11 5.4C11 2.4 8.5 0 5.5 0zm0 7.6A2.2 2.2 0 1 1 5.5 3.2a2.2 2.2 0 0 1 0 4.4z" fill="#16a58a"/></svg>
      2210 Larkspur Ridge Road<br>Fairhaven, NJ 08899
    </div>
    <div class="program" style="left:30px;top:670px;width:330px"><span style="color:var(--ink)">WE ARE A KINDRED</span><br><span style="color:var(--teal)">RX &amp; HEART PROGRAM</span></div>
  </div>

  <div class="col c3 teal">
    <div class="brand" style="left:40px;top:38px;color:var(--white)">
      <span class="mark" style="border:2px solid var(--white);border-radius:50%;width:34px;height:34px"></span>
      <span class="name" style="font-size:27px">Corvenhale<small style="font-size:13px">Twin Pharmacy</small></span>
    </div>
    <div class="title" style="left:36px;top:150px;font-size:38px">Corvenhale</div>
    <div class="title" style="left:36px;top:192px;font-size:29px;font-weight:500">Twin Pharmacy</div>
    <div class="abs" style="left:36px;top:248px;font-size:13.5px;font-weight:500;line-height:1.3">2210 Larkspur Ridge<br>Road<br>Fairhaven, NJ 08899</div>
    <div class="photo" role="img" aria-label="Smiling family of four lying together, father in front" style="left:70px;top:400px;width:280px;height:310px;border-radius:120px 120px 20px 20px;background:linear-gradient(180deg,#e7c1a3,#f3e7de 55%,#ffffff)"></div>
    <div class="badge-ship" style="left:12px;top:318px;width:112px;height:112px"></div>
    <div class="abs contact" style="left:36px;top:748px;font-size:20px;color:var(--white)">
      <div><b style="color:var(--yellow)">Phone:</b> 609-555-0172</div>
      <div><b style="color:var(--yellow)">Toll Free:</b> 800-555-0199</div>
      <div><b style="color:var(--yellow)">Fax:</b> 609-555-0148</div>
    </div>
  </div>
</section>

<!-- INSIDE SPREAD -->
<section class="spread inside">

  <div class="col c1">
    <div class="pill" style="left:28px;top:22px;width:324px">CONFIDENTIAL PRICING FOR<br>SUMMIT FERTILITY COLORADO</div>
    <div class="bracket" style="left:22px;top:142px;width:336px;height:22px;border-bottom:none;background:transparent"></div>
    <h2 class="abs heading meds-title" style="background:var(--white);width:230px;left:75px">MEDICATIONS</h2>
    <table class="med-table">
      <tr><td>Progesterone 100mg capsule each</td><td class="price">$0.00</td></tr>
      <tr><td>Progesterone 200mg capsule each</td><td class="price">$2.00</td></tr>
      <tr><td>Lumavel 8% (per applicator)</td><td class="price">$0.00</td></tr>
      <tr><td>Progesterone in Oil 50mg/ml</td><td class="price">$0.00</td></tr>
      <tr><td>Novaryn 5,000 units</td><td class="price">$0.00</td></tr>
      <tr><td>Ganirelix 250mcg PFS</td><td class="price">$0.00</td></tr>
      <tr><td>Menovra 75</td><td class="price">$0.00</td></tr>
      <tr><td>Pregova 10,000 units</td><td class="price">$0.00</td></tr>
      <tr><td>Cetrolin 250mcg</td><td class="price">$0.00</td></tr>
      <tr><td>Follivar 300</td><td class="price">$0.00</td></tr>
      <tr><td>Follivar 600</td><td class="price">$0.00</td></tr>
      <tr><td>Follivar 900</td><td class="price">$0.00</td></tr>
      <tr><td>Endovira 100mg</td><td class="price">$0.00</td></tr>
      <tr><td>Ovanel 250mcg PFS</td><td class="price">$9.00</td></tr>
      <tr><td>Leuprolide 2-week kit</td><td class="price">$0.00</td></tr>
    </table>
    <div class="bracket" style="left:22px;top:648px;width:240px;height:20px;border-top:none;border-right:none"></div>
    <div class="abs" style="left:0;top:690px;width:380px;height:190px;background:linear-gradient(180deg,#ffffff,#eaf6f3)"></div>
    <div class="brand" style="left:32px;top:755px;color:var(--teal)">
      <span class="mark" style="border:2px solid var(--teal);border-radius:50%;width:28px;height:28px"></span>
      <span class="name" style="font-size:24px">Corvenhale<small>Twin Pharmacy</small></span>
    </div>
    <div class="photo" role="img" aria-label="Smiling female doctor with stethoscope presenting with open hand" style="left:200px;top:675px;width:180px;height:205px;border-radius:80px 80px 0 0;background:linear-gradient(180deg,#7a5a44,#e8cdb8 45%,#f7f7f7)"></div>
  </div>

  <div class="col c2 teal">
    <div class="ivf-box"></div>
    <div class="ivf-title"><span style="background:var(--teal);padding:0 12px">IVF BUNDLE</span></div>
    <div class="ivf-head"><span>Medication name</span><span>Quantity</span></div>
    <table class="ivf-table">
      <tr><td>Endovira</td><td>mg</td></tr>
      <tr><td>Progesterone</td><td>200mg caps</td></tr>
      <tr><td>Ganirelix</td><td>250mg PFS</td></tr>
      <tr><td>Follivar</td><td>300mg</td></tr>
      <tr><td>Pregova</td><td>mg</td></tr>
      <tr><td>Menovra</td><td>mg</td></tr>
      <tr><td>Leuprolide Kit</td><td>mg</td></tr>
    </table>
    <div class="owners">
      <div role="img" aria-label="Two pharmacy owners standing in their pharmacy" style="width:300px;height:165px;background:linear-gradient(180deg,#b44a4a 0,#d8d8d8 22%,#c9c9c9 60%,#3b3b3b)"></div>
      <p>Owners Daniel Marsh RPh and Helen Marsh RPh</p>
    </div>
    <div class="years"><span class="over">OVER</span><span class="big">65 Years!</span></div>
    <div class="serving">Proudly Serving Fairhaven</div>
    <p class="about">We are conveniently located in the Brookline Plaza shopping center on Larkspur Avenue, near the Miller's Market with plenty off street parking. Our current location is bigger and more modern than our previous one but, one thing we've carried over is our good old fashioned friendly service.</p>
  </div>

  <div class="col c3 tint">
    <div class="cert">
      <div class="seal"></div>
      <div class="acc">ACCREDITED</div>
      <div class="exp">Specialty Pharmacy<br>Expires 06/01/2021</div>
    </div>
    <div class="photo" role="img" aria-label="Cheerful family of mother, father and daughter pointing toward the text" style="left:20px;top:250px;width:340px;height:600px;border-radius:150px 150px 10px 10px;background:linear-gradient(180deg,#e9d2bd,#cfe0ec 35%,#9fb6d0 65%,#e9eef3)"></div>
  </div>
</section>

</body>
</html>
```